Make my current Presentation more Professional

I am selling frozen pulp and sorbets. I have a presentation done to introduce the product to customers i want to sell my product to. However the presentation does not have a character - i need to make it look more professional, and at the same time i want to make the product stand out, and have the overall presentation look very fresh, and embedding the true look and feel of what we are offering. 100% NATURAL TROPICAL BRAZILIAN FRUITS.
Some of the text in the presentation is pasted like image, i need it as text.
There should be a specific template that you will use so that i can add remove slides later on according to my requirement

Target Market(s)

Presentation is intended for F&B managers & Chefs in hotels, restaurant

Industry/Entity Type

Food Service

Font styles to use
Sans Serif

Colors

Designer to choose colors to be used in the design.

Requirements
Must have
• A fresh, natural look and feel of tropical fruits.
• It also should come across professional as we are selling products to potential customers.
• I need a clear template - with header, font etc..
Nice to have
• If you want to buy some pictures of fruits, i can buy it for you to make it look great

```html
<!DOCTYPE html>
<html lang="en">
<head>
<meta charset="utf-8">
<title>Frutalia Nativa – Business Presentation Template</title>
<link href="https://fonts.googleapis.com/css2?family=Raleway:wght@400;600;700;800&display=swap" rel="stylesheet">
<style>
:root{
  --green:#168a2c;
  --green-dark:#0e6a22;
  --yellow:#f5c518;
  --red:#b0121d;
  --ink:#1d1d1d;
  --grey:#5b5b5b;
  --canvas:#f0f0f0;
  --white:#ffffff;
  --cream:#f7f2d9;
}
*{box-sizing:border-box;margin:0;padding:0}
html,body{width:1000px;height:1200px;overflow:hidden;background:var(--canvas);font-family:'Raleway',sans-serif;color:var(--ink)}
.page{position:relative;width:1000px;height:1200px}

.slide{position:absolute;width:312px;height:176px;background:var(--white);overflow:hidden;box-shadow:0 1px 3px rgba(0,0,0,.08)}
.hero{left:343px;top:73px;transform:scale(1.122);transform-origin:0 0;box-shadow:0 6px 18px rgba(0,0,0,.15)}

.photo{position:absolute}
.body-copy{position:absolute;font-size:4.3px;line-height:1.55;color:var(--grey)}
.body-copy b{color:var(--ink)}
.title{position:absolute;font-weight:800;line-height:1.1}

.brand{display:inline-flex;align-items:center;gap:3px;font-weight:800;color:var(--green);white-space:nowrap}
.brand::before{content:"";width:.9em;height:.9em;border-radius:50%;background:var(--green);flex:none}

.footer{position:absolute;left:0;right:0;bottom:0;height:9px;background:var(--green)}
.footer .tag{position:absolute;left:6px;top:2px;font-size:3.6px;color:var(--white);white-space:nowrap}
.footer .logo-box{position:absolute;right:0;bottom:0;height:14px;width:62px;background:var(--white);clip-path:polygon(10% 0,100% 0,100% 100%,0 100%);display:flex;align-items:center;justify-content:flex-end;padding-right:8px;font-size:6.5px}
.footer .logo-box::after{content:"";position:absolute;right:0;bottom:0;width:4px;height:9px;background:var(--yellow)}

.deco{position:absolute;border-radius:50%}

/* cover */
.cover-cream{position:absolute;left:150px;top:0;width:162px;height:120px;background:var(--cream);clip-path:polygon(20% 0,100% 0,100% 100%,0 45%)}
.cover-basket{left:170px;top:5px;width:142px;height:120px;background:radial-gradient(circle at 50% 45%,#d9cf68,#b8893c 55%,#6e4a22);clip-path:polygon(25% 0,100% 0,100% 60%,70% 100%,0 40%)}
.cover-green{position:absolute;left:220px;top:90px;width:92px;height:86px;background:var(--green);clip-path:polygon(100% 0,100% 100%,0 100%)}
.cover-oranges{left:105px;top:105px;width:110px;height:90px;background:radial-gradient(circle,#f0902a,#c85f10 60%,#2f5a1e);clip-path:polygon(50% 0,100% 45%,70% 100%,20% 100%,0 70%)}
.cover-text{position:absolute;left:12px;top:48px}
.cover-text .brand{font-size:10px;margin-bottom:6px}
.cover-text h1{font-size:11px;font-weight:800;line-height:1.15}
.cover-text h1 .accent{color:var(--green)}
.cover-text p{font-size:4px;line-height:1.5;color:var(--grey);margin-top:3px;width:130px}

/* about */
.about-photo{left:140px;top:0;width:172px;height:160px;background:radial-gradient(circle at 55% 50%,#d9302a,#a01818 55%,#4d6b2a);clip-path:polygon(0 0,100% 0,100% 100%,55% 100%,25% 55%)}

/* wellness */
.diamond{clip-path:polygon(50% 0,100% 50%,50% 100%,0 50%)}
.well-photo{left:15px;top:18px;width:130px;height:130px;background:radial-gradient(circle,#f08a1e,#d4680f 55%,#2d5a1d)}

/* history */
.history-panel{position:absolute;left:16px;top:0;width:124px;height:142px;border-radius:0 0 10px 10px;background:linear-gradient(160deg,#3aa545,#137a27)}
.history-panel .title{left:10px;top:48px;color:var(--white);font-size:9px}
.history-panel .body-copy{left:10px;top:70px;width:105px;color:#e8f5e9}

/* locations */
.loc-photo{top:0;height:72px;width:74px}

/* vision */
.vision-photo{left:50px;top:0;width:212px;height:110px;background:radial-gradient(circle at 50% 40%,#6fb24a,#2f7a2a 60%,#1b5a1e);clip-path:polygon(8% 0,92% 0,78% 55%,55% 100%,45% 100%,22% 55%)}

/* values */
.value{position:absolute;top:58px;width:40px;text-align:center}
.value .tile{width:28px;height:28px;margin:0 auto;border-radius:6px;transform:rotate(45deg);display:flex;align-items:center;justify-content:center}
.value .tile svg{transform:rotate(-45deg)}
.value span{display:block;margin-top:14px;font-size:4.8px;font-weight:700}

/* product */
.prod-panel{top:10px;width:62px;height:145px}
.prod-panel .cap{position:absolute;left:0;right:0;bottom:8px;height:17px;background:rgba(0,0,0,.55);color:var(--white);font-size:4.8px;font-weight:600;display:flex;align-items:center;justify-content:center}

/* heading text */
.card-photo{top:62px;width:92px;height:52px}
.card{position:absolute;top:118px;width:92px}
.card h3{font-size:5px;font-weight:800;margin-bottom:2px}
.card p{font-size:3.8px;line-height:1.5;color:var(--grey)}

/* watermelon */
.melon-grid{left:0;top:0;width:175px;height:176px;background:linear-gradient(135deg,#c7282d,#e6574f 50%,#8f1515);clip-path:polygon(0 0,70% 0,100% 35%,60% 100%,0 100%)}
.melon-badge{position:absolute;left:112px;top:92px;width:62px;height:62px;background:var(--red);display:flex;align-items:center;justify-content:center;text-align:center;color:var(--white);font-size:5px;font-weight:700;line-height:1.3}

/* customers */
.crowd-bg{left:0;top:0;width:312px;height:176px;background:radial-gradient(circle at 60% 50%,#f3e6c4,#e2c58e 60%,#c9a36a)}
.cust{width:48px;height:62px}
</style>
</head>
<body>
<main class="page">

  <!-- Hero cover -->
  <section class="slide hero" aria-label="Cover slide">
    <div class="cover-cream"></div>
    <div class="photo cover-basket" role="img" aria-label="Photo of a wicker basket of grapes, bananas and peaches"></div>
    <div class="cover-green"></div>
    <div class="photo cover-oranges" role="img" aria-label="Photo of fresh oranges with leaves"></div>
    <div class="cover-text">
      <div class="brand">Frutalia Nativa</div>
      <h1><span class="accent">BUSINESS</span><br>POWERPOINT TEMPLATE</h1>
      <p>Fresh pulp from ripe fruit, made with care, per ea mails soluta, frozen to keep taste.</p>
    </div>
  </section>

  <!-- Row 1 -->
  <section class="slide" style="left:19px;top:352px" aria-label="Cover slide">
    <div class="cover-cream"></div>
    <div class="photo cover-basket" role="img" aria-label="Photo of a wicker basket of grapes, bananas and peaches"></div>
    <div class="cover-green"></div>
    <div class="photo cover-oranges" role="img" aria-label="Photo of fresh oranges with leaves"></div>
    <div class="cover-text">
      <div class="brand">Frutalia Nativa</div>
      <h1><span class="accent">BUSINESS</span><br>POWERPOINT TEMPLATE</h1>
      <p>Fresh pulp from ripe fruit, made with care, per ea mails soluta, frozen to keep taste.</p>
    </div>
  </section>

  <section class="slide" style="left:347px;top:352px" aria-label="About slide">
    <div class="photo about-photo" role="img" aria-label="Photo of a bowl of red apples"></div>
    <div class="title" style="left:14px;top:40px;font-size:9px"><span style="color:var(--red)">About</span><br><span style="color:var(--grey)">Frutalia Nativa</span></div>
    <p class="body-copy" style="left:14px;top:72px;width:148px">Frutalia fruit pulp is <b>100% made of selected tropical fruit</b> processed at the optimal stage of ripeness according to a simple but accurate production process. <b>No sugar, preservatives or colorings are added.</b></p>
    <p class="body-copy" style="left:14px;top:112px;width:148px">The nutritional qualities of fresh tropical fruits are kept intact. All drinks, sorbets and bowls made with our pulp are ideal for fresh juices and smoothies, a daily complement for everybody's diet.</p>
    <div class="footer"><span class="tag">100% Natural Tropical Brazilian Fruits</span><span class="logo-box"><span class="brand">Frutalia</span></span></div>
  </section>

  <section class="slide" style="left:675px;top:352px" aria-label="Fruits of wellness slide">
    <div class="deco" role="img" aria-label="Lime illustration" style="left:30px;top:-6px;width:18px;height:14px;background:#8cc63f"></div>
    <div class="deco" role="img" aria-label="Lemon slice illustration" style="left:286px;top:12px;width:20px;height:20px;background:var(--yellow)"></div>
    <div class="deco" role="img" aria-label="Orange illustration" style="left:2px;top:130px;width:20px;height:20px;background:#f08a1e"></div>
    <div class="photo diamond well-photo" role="img" aria-label="Photo of fresh oranges with leaves"></div>
    <div class="title" style="left:158px;top:62px;font-size:11px">The <span style="color:var(--yellow)">Fruits</span><br><span style="color:var(--green)">Of Wellness</span></div>
    <p class="body-copy" style="left:158px;top:98px;width:140px">Discover the unique taste of the best tropical fruits from South America. With our pulp you can enjoy smoothies, vitamins and all the fruit specialties with new and fascinating exotic varieties that contain numerous and extra ordinary healing properties.</p>
    <div class="footer"><span class="tag">100% Natural Tropical Brazilian Fruits</span><span class="logo-box"><span class="brand">Frutalia</span></span></div>
  </section>

  <!-- Row 2 -->
  <section class="slide" style="left:19px;top:542px" aria-label="History slide">
    <div class="history-panel" role="img" aria-label="Green photo of grape vines behind the panel">
      <div class="title">Our<br>Hystory</div>
      <p class="body-copy">Frutalia Nativa was brought to the region by Monte Holding Ltd as master franchisee, with the aim of sharing our products. Its aim is to grow through shops and retailing of the pulps. The first rights to open were granted to Lina &amp; Co Trading L.L.C.</p>
    </div>
    <div class="deco" role="img" aria-label="Watermelon slice illustration" style="left:284px;top:2px;width:22px;height:22px;background:#e0353a"></div>
    <p class="body-copy" style="left:162px;top:40px;width:138px"><b>Lina &amp; Co Trading L.L.C</b> opened their first Frutalia shop in February 2014, which is a franchise with locations in several cities. The concept of Frutalia lies in using frozen exotic fruit pulps which are 100% natural without preservatives or colorants in preparing tasty vitamins, sorbets and the famous fruit bowl. This wide variety of fruit pulps is unavailable anywhere else in the region. These pulps have premium characteristics, nutritional value and the highest quality in terms of consistency of flavour and color.</p>
    <div class="footer"><span class="tag">100% Natural Tropical Brazilian Fruits</span><span class="logo-box"><span class="brand">Frutalia</span></span></div>
  </section>

  <section class="slide" style="left:347px;top:542px" aria-label="Locations slide">
    <div class="photo loc-photo" role="img" aria-label="Photo of the food truck outside" style="left:0;background:linear-gradient(#d9c9a0,#6b7a3a)"></div>
    <div class="photo loc-photo" role="img" aria-label="Photo of the shop front" style="left:78px;background:linear-gradient(#7a9a4a,#3a5a2a)"></div>
    <div class="photo loc-photo" role="img" aria-label="Photo of staff meeting at the shop" style="left:156px;background:linear-gradient(#b8a488,#5a4a3a)"></div>
    <div class="photo loc-photo" role="img" aria-label="Photo of the team at a counter" style="left:234px;width:78px;background:linear-gradient(#8a8070,#3a3530)"></div>
    <div class="title" style="left:16px;top:96px;font-size:8.5px;font-weight:700"><span style="color:var(--ink)">Our</span><br><span style="color:var(--green)">Locations</span></div>
    <p class="body-copy" style="left:16px;top:122px;width:262px">We are located in the prestigious area of The Palm Walk, close to new cinemas with a view of the majestic beachfront. Our newest shop is in Harbor Care Hospital in the capital. We also have a food truck on the beach.</p>
    <div class="deco" role="img" aria-label="Pineapple illustration" style="left:286px;top:82px;width:18px;height:24px;background:#f0b31e"></div>
    <div class="deco" role="img" aria-label="Peach illustration" style="left:276px;top:136px;width:16px;height:16px;background:#f29a4a"></div>
    <div class="footer"><span class="tag">100% Natural Tropical Brazilian Fruits</span><span class="logo-box"><span class="brand">Frutalia</span></span></div>
  </section>

  <section class="slide" style="left:675px;top:542px" aria-label="Vision and mission slide">
    <div class="photo vision-photo" role="img" aria-label="Green-toned photo of tropical fruit"></div>
    <div class="brand" style="position:absolute;left:118px;top:42px;font-size:11px;color:var(--white)">Frutalia Nativa</div>
    <div class="deco" role="img" aria-label="Pineapple illustration" style="left:90px;top:68px;width:14px;height:18px;background:#f0b31e"></div>
    <div class="deco" role="img" aria-label="Lemon slice illustration" style="left:238px;top:28px;width:16px;height:16px;background:var(--yellow)"></div>
    <div class="title" style="left:14px;top:90px;font-size:8px;color:var(--green)">Vision</div>
    <p class="body-copy" style="left:14px;top:106px;width:100px">To become the number one company providing high quality fruit pulps, vitamins, sorbets &amp; gelato.</p>
    <div class="title" style="right:14px;top:90px;font-size:8px;color:var(--green)">Mision</div>
    <p class="body-copy" style="right:14px;top:106px;width:120px;text-align:right">To continuously provide consistent quality with utmost customer satisfaction and services while bearing in mind exceeding their expectations at all times, combined with team motivation, training and a good team spirit.</p>
    <div class="footer"><span class="tag">100% Natural Tropical Brazilian Fruits</span><span class="logo-box"><span class="brand">Frutalia</span></span></div>
  </section>

  <!-- Row 3 -->
  <section class="slide" style="left:19px;top:731px" aria-label="Values slide">
    <div class="deco" role="img" aria-label="Lemon slice illustration" style="left:284px;top:4px;width:24px;height:24px;background:var(--yellow)"></div>
    <div class="deco" role="img" aria-label="Watermelon slice illustration" style="left:0;top:134px;width:16px;height:16px;background:#e0353a"></div>
    <div class="title" style="left:0;right:0;top:18px;text-align:center;font-size:10px">Our Values</div>
    <div style="position:absolute;left:0;right:0;top:33px;text-align:center;font-size:4.5px;color:var(--grey)">Sub Heading Text Here</div>
    <div class="value" style="left:23px"><div class="tile" style="background:var(--green)"><svg width="14" height="14" viewBox="0 0 14 14" fill="none" stroke="#fff" stroke-width="1"><circle cx="7" cy="7" r="5"/><circle cx="7" cy="7" r="1.5"/></svg></div><span>Customer<br>Focus</span></div>
    <div class="value" style="left:79px"><div class="tile" style="background:var(--yellow)"><svg width="14" height="14" viewBox="0 0 14 14" fill="none" stroke="#fff" stroke-width="1"><circle cx="7" cy="7" r="5"/><path d="M4.5 8.2q2.5 2.2 5 0"/><circle cx="5.2" cy="5.6" r=".5" fill="#fff"/><circle cx="8.8" cy="5.6" r=".5" fill="#fff"/></svg></div><span>Happy</span></div>
    <div class="value" style="left:135px"><div class="tile" style="background:var(--green)"><svg width="14" height="14" viewBox="0 0 14 14" fill="none" stroke="#fff" stroke-width="1"><circle cx="7" cy="5" r="2"/><path d="M3 12q4-6 8 0"/></svg></div><span>Teamwork</span></div>
    <div class="value" style="left:191px"><div class="tile" style="background:var(--yellow)"><svg width="14" height="14" viewBox="0 0 14 14" fill="none" stroke="#fff" stroke-width="1"><path d="M7 11.5 2.8 7.2a2.3 2.3 0 0 1 4.2-3 2.3 2.3 0 0 1 4.2 3z"/></svg></div><span>Integrity</span></div>
    <div class="value" style="left:247px"><div class="tile" style="background:var(--green)"><svg width="14" height="14" viewBox="0 0 14 14" fill="none" stroke="#fff" stroke-width="1"><circle cx="7" cy="7" r="1.5"/><ellipse cx="7" cy="7" rx="5" ry="2"/><ellipse cx="7" cy="7" rx="2" ry="5"/></svg></div><span>Energy</span></div>
    <div class="footer"><span class="tag">100% Natural Tropical Brazilian Fruits</span><span class="logo-box"><span class="brand">Frutalia</span></span></div>
  </section>

  <section class="slide" style="left:347px;top:731px" aria-label="Product slide">
    <div class="title" style="left:12px;top:54px;font-size:10px"><span>Our</span><br><span style="color:var(--green)">Product</span></div>
    <p class="body-copy" style="left:12px;top:88px;width:88px">Qui et modo necessitatibus. Vix cu wisi assentior, ut quo debet ullamcorper, ei nam quas albucius. Scripta inermis comprehensam eum no, harum indoctum cu his. Cu vim quando omnesque consulatu, te solum quaeque incorrupte vim, possit laoreet.</p>
    <div class="photo prod-panel" role="img" aria-label="Photo of a sliced lime" style="left:106px;background:radial-gradient(circle at 50% 35%,#d9ec8a,#8dbf2e 55%,#2a2a2a)"><div class="cap">Pulps Variety</div></div>
    <div class="photo prod-panel" role="img" aria-label="Photo of green smoothies in glasses" style="left:172px;background:linear-gradient(#f2f0d8,#c9d98a 55%,#7a8a3a)"><div class="cap">Smoothies</div></div>
    <div class="photo prod-panel" role="img" aria-label="Photo of red fruit sorbet bars" style="left:238px;background:linear-gradient(#c42a2a,#8a1010 60%,#3a1a10)"><div class="cap">Sorbetti</div></div>
    <div class="footer"><span class="tag">100% Natural Tropical Brazilian Fruits</span><span class="logo-box"><span class="brand">Frutalia</span></span></div>
  </section>

  <section class="slide" style="left:675px;top:731px" aria-label="Food cart slide">
    <div class="photo" role="img" aria-label="Photo of a green sorbet cart" style="left:6px;top:18px;width:78px;height:78px;background:linear-gradient(#e8eadf,#b9c7a6)"></div>
    <div class="photo" role="img" aria-label="Photo of an orange-roofed sorbet cart" style="left:90px;top:62px;width:92px;height:92px;background:linear-gradient(#f1ece3,#c8b8a0)"></div>
    <div class="title" style="left:188px;top:56px;font-size:9px;font-weight:700">Your<br><span style="color:var(--green)">Text Here</span></div>
    <p class="body-copy" style="left:188px;top:84px;width:112px">Qui et modo necessitatibus. Vix cu wisi assentior, ut quo debet ullamcorper, ei nam quas albucius. Scripta inermis comprehensam eum no, harum indoctum cu his. Cu vim quando omnesque consulatu, te solum quaeque incorrupte vim, possit laoreet prodesset vis id.</p>
    <div class="footer"><span class="tag">100% Natural Tropical Brazilian Fruits</span><span class="logo-box"><span class="brand">Frutalia</span></span></div>
  </section>

  <!-- Row 4 -->
  <section class="slide" style="left:19px;top:920px" aria-label="Three column slide">
    <div class="deco" role="img" aria-label="Leaf illustration" style="left:298px;top:4px;width:14px;height:14px;background:#5aa83a"></div>
    <div class="deco" role="img" aria-label="Orange illustration" style="left:0;top:36px;width:14px;height:14px;background:#f08a1e"></div>
    <div class="title" style="left:0;right:0;top:18px;text-align:center;font-size:10px">Heading Text</div>
    <div style="position:absolute;left:0;right:0;top:32px;text-align:center;font-size:4.5px;color:var(--grey)">Sub Heading Text Here</div>
    <div class="photo card-photo" role="img" aria-label="Photo of dark grapes on the vine" style="left:12px;background:radial-gradient(circle,#5a3a5a,#2a4a1e)"></div>
    <div class="photo card-photo" role="img" aria-label="Photo of oranges" style="left:110px;background:radial-gradient(circle,#f08a1e,#b85a10 60%,#2d5a1d)"></div>
    <div class="photo card-photo" role="img" aria-label="Photo of a fruit basket" style="left:208px;background:radial-gradient(circle,#d9cf68,#b8893c 55%,#f0ece0)"></div>
    <div class="card" style="left:12px"><h3>Heading Text</h3><p>Qui et modo necessitatibus. Vix cu wisi assentior, ut quo debet ullamcorper, ei nam quas albucius.</p></div>
    <div class="card" style="left:110px"><h3>Heading Text</h3><p>Qui et modo necessitatibus. Vix cu wisi assentior, ut quo debet ullamcorper, ei nam quas albucius.</p></div>
    <div class="card" style="left:208px"><h3>Heading Text</h3><p>Qui et modo necessitatibus. Vix cu wisi assentior, ut quo debet ullamcorper, ei nam quas albucius.</p></div>
    <div class="footer"><span class="tag">100% Natural Tropical Brazilian Fruits</span><span class="logo-box"><span class="brand">Frutalia</span></span></div>
  </section>

  <section class="slide" style="left:347px;top:920px" aria-label="Watermelon feature slide">
    <div class="photo melon-grid" role="img" aria-label="Tiled photos of watermelon slices and sorbet bars"></div>
    <div class="melon-badge diamond"><span>Fresh<br>Watermelon<br>Sliced</span></div>
    <div class="title" style="right:16px;top:82px;font-size:9px;font-weight:700;text-align:right">Your<br><span style="color:var(--red)">Text Here</span></div>
    <p class="body-copy" style="right:16px;top:110px;width:126px;text-align:right">Qui et modo necessitatibus. Vix cu wisi assentior, ut quo debet ullamcorper, ei nam quas albucius. Scripta inermis comprehensam eum no, harum indoctum cu his. Cu vim quando omnesque consulatu, te solum quaeque incorrupte vim, possit laoreet prodesset vis id.</p>
  </section>

  <section class="slide" style="left:675px;top:920px" aria-label="Happy customers slide">
    <div class="photo crowd-bg" role="img" aria-label="Soft blurred photo of a sunny shop interior"></div>
    <div class="deco" role="img" aria-label="Watermelon slice illustration" style="left:2px;top:8px;width:20px;height:20px;background:#e0353a"></div>
    <div class="deco" role="img" aria-label="Lemon slice illustration" style="left:286px;top:150px;width:24px;height:24px;background:var(--yellow)"></div>
    <div class="title" style="left:26px;top:16px;font-size:9px;font-weight:700">Our Happy <span style="color:var(--green)">Customer</span></div>
    <div class="photo cust" role="img" aria-label="Customer photo" style="left:26px;top:36px;background:#b9a38a"></div>
    <div class="photo cust" role="img" aria-label="Customer photo" style="left:78px;top:36px;background:#c7a56a"></div>
    <div class="photo cust" role="img" aria-label="Customer photo" style="left:130px;top:36px;background:#9fb7c9"></div>
    <div class="photo cust" role="img" aria-label="Customer photo" style="left:182px;top:36px;width:104px;background:#d6b58a"></div>
    <div class="photo cust" role="img" aria-label="Customer photo" style="left:26px;top:102px;background:#8a6a4a"></div>
    <div class="photo cust" role="img" aria-label="Customer photo" style="left:78px;top:102px;background:#a58a6a"></div>
    <div class="photo cust" role="img" aria-label="Customer photo" style="left:130px;top:102px;background:#7a6a5a"></div>
    <div class="photo cust" role="img" aria-label="Customer photo" style="left:182px;top:102px;background:#c9b48a"></div>
    <div class="photo cust" role="img" aria-label="Customer photo" style="left:234px;top:102px;width:52px;background:#b99a7a"></div>
  </section>

</main>
</body>
</html>
```